Full 10+ Page Online Learning eBook Design - NOT just the cover :)

We currently have an eBook within the online learning space which is geared towards a consumer audience (hobbyists, interests), but we have a new 2.0 version which is geared towards professionals (certifications, training, continuing ed, career-oriented). We need a new design and need the words/copy put into the eBook, but want to keep the look and feel of the original (open to variations in design). File is attached, along with various logo options.

Target Market(s)

Professionals

Industry/Entity Type

Learning

Font styles to use
Sans Serif

Colors
33a6d7
acd036
919191

Requirements
Must have
• Must follow a very similar look a feel of the original file. We use a lot of fonts like Raleway, Gotham, Helvetica Neue, Gil Sans, DIN - anything modern looking. We also use a lot of grayish hexagons in our corporate design. Feel free to check out brightlanternworks.example to get a better sense.
Nice to have
• Include some professionally oriented icons / photos
Should not have
• No cartoonish graphics or imagery

```html
<!DOCTYPE html>
<html lang="en">
<head>
<meta charset="utf-8">
<title>Scaling a Learning Business</title>
<link href="https://fonts.googleapis.com/css2?family=Cabin:wght@400;500&family=Montserrat:wght@400&display=swap" rel="stylesheet">
<style>
  :root {
    --page: #ffffff;
    --ink: #1f1f1f;
    --heading: #111111;
    --rule: #919191;
    --night-deep: #0d1426;
    --night-mid: #1c2a4a;
    --city-glow: #c9883a;
    --city-amber: #e6a24a;
  }
  * { margin: 0; padding: 0; box-sizing: border-box; }
  html, body { width: 852px; height: 1200px; overflow: hidden; background: var(--page); }
  .page { position: relative; width: 852px; height: 1200px; background: var(--page); }
  .hero-photo {
    position: absolute; left: 0; top: 0; width: 852px; height: 312px;
    background:
      radial-gradient(ellipse 60% 45% at 70% 85%, rgba(230,162,74,0.55), transparent 70%),
      radial-gradient(ellipse 30% 40% at 45% 40%, rgba(201,136,58,0.35), transparent 70%),
      linear-gradient(180deg, var(--night-mid) 0%, #27406b 35%, #3a3d4e 70%, #5a4330 100%);
  }
  .footer-photo {
    position: absolute; left: 0; top: 930px; width: 852px; height: 270px;
    background:
      radial-gradient(ellipse 70% 40% at 55% 85%, rgba(230,162,74,0.6), transparent 70%),
      radial-gradient(ellipse 25% 35% at 35% 55%, rgba(201,136,58,0.4), transparent 70%),
      linear-gradient(180deg, #2b3c5e 0%, #3b4a66 30%, #4a3e36 65%, #6b4a28 100%);
  }
  .article { position: absolute; left: 7px; top: 334px; width: 840px; }
  .article-title {
    font-family: "Cabin", sans-serif; font-weight: 400; font-size: 19.5px;
    color: var(--heading); letter-spacing: 0.2px; line-height: 24px;
    padding-bottom: 5px; border-bottom: 2.5px solid var(--rule); margin-bottom: 12px;
  }
  .article p {
    font-family: "Montserrat", sans-serif; font-size: 15.3px; line-height: 21px;
    color: var(--ink); margin-bottom: 24px; width: 830px;
  }
</style>
</head>
<body>
<div class="page">
  <div class="hero-photo" role="img" aria-label="Aerial view of a city skyline of skyscrapers lit up at night"></div>

  <article class="article">
    <h1 class="article-title">SCALING A LEARNING BUSINESS</h1>
    <p>Building your learning business is no longer limited to the number of hours you can contract out your lead trainer or the number of stores where you can place your best-selling books. Now it's a matter of developing an online presence that can adapt quickly to your changing market opportunities.</p>
    <p>Frequently, we find that learning companies have hit a ceiling. While they may have the content, expertise and business team in place to expand their operations, they lack the technology to connect that infrastructure to customers and prospects. Or maybe they're on a legacy learning management system that now caters to a different kind of user. Or perhaps the LMS was developed in-house and the IT organization has other priorities right now, preventing them from addressing upgrades needed by the online learning business.</p>
    <p>Software-as-a-service provides the most direct route to scalability for a learning business. The company behind the application is typically dedicated to serving the given market, which means interest will never flag.</p>
    <p>Because you pay on a recurring contract for just the services you need, you can scale up or back as the business warrants.</p>
    <p>Just as important, feature development is driven by the needs and demands of all of the clients the SaaS company has, baking technology innovation in as an on-going activity. For example, our own company introduces about 200 new features a year. What you subscribe to today is different from what you'll have six months from now, ensuring that you'll continue getting those features that will help you grow and optimize your business. While we, the SaaS service provider, concentrates on platform development, you can focus on content and monetization.</p>
  </article>

  <div class="footer-photo" role="img" aria-label="City skyline at dusk with towers and glowing streets stretching toward the waterfront"></div>
</div>
</body>
</html>
```